Gemstone Jewelry Online Shop Needs a Banner Design

We need a banner design for a new gemstone Jewelry Online Shop based in the U.S. called "Lumorra". One of our selling points is "never fall out of stone". We want to express: a Party Queen doesn't need to worry whenever she may meet an embarrassing moment - a stone of jewelry falls out at a very important occasion. Please insert one of attached images. Please visit our website for more details: http://lumorra-example.com/
The banner size: 1200*628
If you think other images at our website are better, please let us know. Many thanks and looking forward to your beautiful and creative designs!

Industry/Entity Type

Jewelry

```html
<!DOCTYPE html>
<html lang="en">
<head>
<meta charset="utf-8">
<title>Lumorra – Never fall out of stone</title>
<link rel="stylesheet" href="https://fonts.googleapis.com/css2?family=Alegreya:wght@400;500&family=Montserrat:wght@500&display=swap">
<style>
  :root {
    --stage: #000000;
    --green-deep: #6fb82a;
    --green-mid: #97d03a;
    --green-light: #c8ea7a;
    --green-glow: #e4f6b4;
    --ink: #22197a;
    --logo-ink: #141414;
    --accent-red: #d8262a;
    --band-light: rgba(245, 252, 220, 0.85);
    --photo-silver: #eef0f3;
    --photo-shade: #d6dbe2;
    --photo-tint: #cfc6ee;
  }
  * { margin: 0; padding: 0; box-sizing: border-box; }
  html, body {
    width: 1200px; height: 775px; overflow: hidden;
    background: var(--stage);
  }
  .banner {
    position: absolute; left: 19px; top: 86px;
    width: 1160px; height: 608px; overflow: hidden;
    background:
      radial-gradient(circle at 86% 22%, var(--green-glow) 0%, rgba(228,246,180,0.6) 14%, rgba(200,234,122,0) 34%),
      radial-gradient(circle at 12% 92%, rgba(220,244,170,0.7) 0%, rgba(220,244,170,0) 22%),
      linear-gradient(120deg, var(--green-deep) 0%, var(--green-mid) 38%, var(--green-light) 70%, var(--green-mid) 100%);
    font-family: "Alegreya", Georgia, serif;
    color: var(--ink);
  }
  .banner__swooshes { position: absolute; inset: 0; width: 100%; height: 100%; }
  .brand {
    position: absolute; left: 72px; top: 54px;
  }
  .brand__name {
    font-family: "Alegreya", Georgia, serif;
    font-weight: 400; font-size: 100px; line-height: 1;
    color: var(--logo-ink);
  }
  .brand__tagline {
    font-family: "Montserrat", Arial, sans-serif;
    font-weight: 500; font-size: 14px; letter-spacing: 0.3px;
    color: var(--accent-red);
    margin: 8px 0 0 125px;
  }
  .headline {
    position: absolute; left: 620px; width: 460px; top: 96px;
    text-align: center;
    font-size: 47px; font-weight: 500; line-height: 1;
  }
  .message {
    position: absolute; left: 103px; width: 640px; top: 272px;
    text-align: center;
    font-size: 30px; line-height: 48px;
  }
  .site-link {
    position: absolute; left: 103px; width: 640px; top: 532px;
    text-align: center;
    font-size: 30px; line-height: 1;
  }
  .product-photo {
    position: absolute; left: 785px; top: 210px;
    width: 304px; height: 328px;
    border-radius: 18px;
    background: linear-gradient(150deg, var(--photo-tint) 0%, var(--photo-silver) 40%, var(--photo-shade) 100%);
    opacity: 0.9;
  }
</style>
</head>
<body>
  <main class="banner">
    <svg class="banner__swooshes" viewBox="0 0 1160 608" preserveAspectRatio="none" aria-hidden="true">
      <path d="M0 0 H600 C560 110 420 150 0 232 Z" fill="rgba(100,170,30,0.45)"/>
      <path d="M0 232 C200 190 400 170 540 158 C600 150 660 130 700 110 C660 150 600 170 540 176 C400 186 200 210 0 252 Z" fill="var(--band-light)"/>
      <path d="M0 252 C160 220 320 200 460 192 C320 210 160 236 0 272 Z" fill="rgba(255,255,255,0.25)"/>
      <path d="M40 608 C220 420 460 300 760 180" stroke="rgba(255,255,255,0.28)" stroke-width="3" fill="none"/>
      <path d="M260 608 C420 470 620 380 1160 250" stroke="rgba(255,255,255,0.22)" stroke-width="2" fill="none"/>
      <path d="M560 608 C700 500 900 420 1160 380" stroke="rgba(255,255,255,0.2)" stroke-width="2" fill="none"/>
      <path d="M500 0 C560 160 720 320 1000 608" stroke="rgba(255,255,255,0.18)" stroke-width="3" fill="none"/>
    </svg>

    <div class="brand">
      <div class="brand__name">Lumorra</div>
      <div class="brand__tagline">FINE GEMSTONE JEWELRY</div>
    </div>

    <h1 class="headline">Never fall out of stone</h1>

    <p class="message">
      A Party Queen doesn't need to worry whenever<br>
      she may meet an embarrassing moment<br>
      - a stone of jewelry falls out at a very<br>
      important occasion
    </p>

    <p class="site-link">visit: http://lumorra-example.com/</p>

    <div class="product-photo" role="img" aria-label="Product photo: silver ring with an oval purple gemstone in a halo of small clear stones"></div>
  </main>
</body>
</html>
```